Webdesign für Juwelier-Geschäft
Zielgruppe
Wir sind ein Juwelier Laden. Unsere Zielgruppe sind Frauen und Männer jeden Alters, die an Gold- und Silberschmuck/Uhren/Diamanten/Trauringen interessiert sind.
Aufgabenstellung
Edles Design in Gold, Schwarz/Grau, Weiß.
Bildelemente für die Artikelkategorien Ketten, Ohrringe und Ringe etc.
Ein Logo besteht bereits.

```html
<!DOCTYPE html>
<html lang="de">
<head>
<meta charset="utf-8">
<title>Juwelier Orvano – Trauringe, Uhren, Schmuck</title>
<link rel="stylesheet" href="https://fonts.googleapis.com/css2?family=Libre+Caslon+Display&family=Inter:wght@400;500;600;700&display=swap">
<style>
:root{
  --gold:#d9a13c;
  --gold-soft:#ebcf98;
  --gold-pale:#f4dfb8;
  --cream:#fdf5e8;
  --navy:#1d1b4c;
  --ink:#1f1f2a;
  --grey:#6f6f7c;
  --line:#ececf0;
  --blush:#e6cdc2;
  --white:#ffffff;
}
*{box-sizing:border-box;margin:0;padding:0}
html,body{width:1200px;height:3226px;overflow:hidden;background:var(--white)}
body{position:relative;font-family:"Inter",Helvetica,Arial,sans-serif;color:var(--ink)}
.abs{position:absolute}
.serif{font-family:"Libre Caslon Display","Times New Roman",serif;font-weight:400;color:var(--navy);letter-spacing:-0.5px}
.serif em{font-style:normal;color:var(--gold)}
.dot{position:absolute;border-radius:50%;background:var(--gold-soft)}

/* navigation */
.nav{left:137px;top:23px;width:924px;height:76px;background:var(--white);border-radius:6px;box-shadow:0 8px 24px rgba(40,30,10,.08)}
.brand{position:absolute;left:40px;top:16px;text-align:center;line-height:1}
.brand-name{font-family:"Libre Caslon Display",serif;font-size:24px;color:var(--navy);letter-spacing:.5px;display:flex;align-items:center;gap:6px}
.brand-name i{display:inline-block;width:10px;height:10px;border-radius:50%;background:var(--gold)}
.brand-sub{font-size:6px;letter-spacing:.6px;color:var(--navy);margin-top:5px}
.menu{position:absolute;top:31px;left:190px;display:flex;font-size:11px;color:#545470}
.menu span{position:relative;margin-right:0}
.menu .active{font-weight:600;color:var(--ink)}
.menu .active:after{content:"";position:absolute;left:50%;top:21px;width:4px;height:4px;margin-left:-2px;border-radius:50%;background:var(--gold)}
.nav-icons{position:absolute;right:56px;top:28px;display:flex;gap:12px}

/* hero panels */
.panel{overflow:hidden}
.panel .bg{position:absolute;inset:0}
.photo{position:absolute;inset:0}
.hero{left:162px;top:129px;width:874px;height:411px}
.hero .bg{background:linear-gradient(100deg,#ffffff 35%,#f7e9e3 70%,var(--blush) 100%)}
.hero .photo{background:linear-gradient(160deg,#efd6c6,#cfa58e 60%,#b98a73);clip-path:polygon(0 0,55.6% 0,23% 100%,0 100%)}
h1,h2{font-weight:400}
.hero h1{position:absolute;left:450px;top:80px;font-size:46px;line-height:48px}
.lead{position:absolute;font-size:11px;line-height:21px;color:var(--grey)}
.btn{position:absolute;display:flex;align-items:center;justify-content:center;border-radius:22px;font-size:11px}
.btn-soft{background:var(--gold-pale);color:var(--white)}
.btn-line{border:1.5px solid var(--navy);color:var(--navy);background:transparent}
.btn-gold{background:var(--gold);color:var(--white)}

/* offer */
.offer{left:84px;top:676px;width:1045px;height:485px;background:var(--cream);border-radius:26px}
.tag{position:absolute;height:23px;border-radius:12px;background:var(--gold-pale);color:var(--gold);font-size:10px;font-weight:700;letter-spacing:2px;display:flex;align-items:center;justify-content:center}
.tag.on-cream{background:#fbe6c2}
.tag.on-white{background:var(--white)}
.section-title{position:absolute;left:0;right:0;text-align:center;font-size:38px}
.cat{position:absolute;top:195px;width:230px;text-align:center}
.cat .icon{width:130px;height:130px;margin:0 auto;border-radius:50%;background:radial-gradient(circle,#f6ecdf 0,#fff 70%);box-shadow:0 0 0 1px #fff}
.cat h3{font-size:15px;font-weight:600;margin-top:25px;color:var(--ink)}
.cat p{font-size:9px;line-height:16px;color:var(--grey);margin-top:10px}
.cat .more{width:38px;height:20px;margin:15px auto 0;border-radius:10px;background:#fbe0b2;color:var(--gold);font-size:8px;line-height:20px}

/* style section */
.style{left:162px;top:1243px;width:874px;height:412px}
.style .bg{background:linear-gradient(100deg,#ffffff 38%,#f8ebe5 70%,#dcc0b6 100%)}
.style .photo{background:linear-gradient(150deg,#f3f3f1,#dcdad6 55%,#bfb8b0);clip-path:polygon(0 0,54.3% 0,21% 100%,0 100%)}
.style h2{position:absolute;left:467px;top:60px;font-size:37px;line-height:41px}

/* testimonials */
.reviews{left:78px;top:1809px;width:1043px;height:634px;background:var(--cream);border-radius:26px}
.review{position:absolute;top:2048px;width:362px;height:252px;background:var(--white);border-radius:24px;box-shadow:0 10px 30px rgba(120,90,40,.06);overflow:hidden}
.review h4{position:absolute;left:35px;top:33px;font-size:14px;font-weight:700}
.review p{position:absolute;left:35px;top:64px;width:300px;font-size:11px;line-height:22px;color:var(--grey)}
.avatar{position:absolute;border-radius:50%;background:linear-gradient(150deg,#f0c9b2,#9b6e5a)}
.review .avatar{left:35px;top:178px;width:42px;height:42px}
.review .who{position:absolute;left:95px;top:182px;font-size:12px;font-weight:600}
.review .who small{display:block;font-size:8px;font-weight:400;color:var(--grey);margin-top:6px}
.arrow-btn{position:absolute;width:48px;height:48px;border-radius:50%;display:flex;align-items:center;justify-content:center}

/* shop banner */
.shop{left:162px;top:2519px;width:874px;height:288px}
.shop .bg{background:linear-gradient(260deg,#ffffff 40%,#f7e9e3 70%,#dfc3b8 100%)}
.shop .photo{background:linear-gradient(200deg,#b77a73,#e6ddd6 45%,#f1ece8);clip-path:polygon(47.8% 0,100% 0,100% 100%,67.5% 100%)}
.shop h2{position:absolute;left:57px;top:70px;font-size:37px;line-height:41px}

/* footer */
.mail{left:162px;top:2958px;font-size:29px}
.social{left:162px;top:3047px;display:flex;align-items:center;gap:11px;font-size:11px;color:var(--grey)}
.social .ring{width:40px;height:40px;border-radius:50%;border:1px solid var(--line)}
.social .label{margin-right:9px}
.links-title{left:638px;top:2905px;font-size:11px;letter-spacing:2px;font-weight:600;color:#9a9aa6}
.link{position:absolute;font-size:14px;color:#3a3a4c}
.copyright{left:0;width:1124px;top:3167px;text-align:center;font-size:11px;color:var(--grey)}
</style>
</head>
<body>

<!-- navigation -->
<header class="abs nav">
  <div class="brand">
    <div class="brand-name">ORVANO <i></i></div>
    <div class="brand-sub">TRAURINGE | UHREN | SCHMUCK</div>
  </div>
  <nav class="menu">
    <span class="active" style="margin-left:0">Start</span>
    <span style="margin-left:52px">Trauringe ⌄</span>
    <span style="margin-left:30px">Reparaturen ⌄</span>
    <span style="margin-left:44px">Über uns</span>
    <span style="margin-left:30px">Shop</span>
  </nav>
  <div class="nav-icons">
    <svg width="18" height="18" viewBox="0 0 24 24" fill="none" stroke="#1f1f2a" stroke-width="2"><path d="M12 20s-7-4.5-7-10a4 4 0 0 1 7-2.5A4 4 0 0 1 19 10c0 5.5-7 10-7 10z"/></svg>
    <svg width="18" height="18" viewBox="0 0 24 24" fill="none" stroke="#1f1f2a" stroke-width="2"><circle cx="10" cy="10" r="6"/><path d="M15 15l5 5"/></svg>
    <svg width="22" height="18" viewBox="0 0 26 24" fill="none" stroke="#1f1f2a" stroke-width="2"><path d="M2 3h3l3 12h11l2-8H7"/><circle cx="9" cy="20" r="1.5"/><circle cx="18" cy="20" r="1.5"/><circle cx="22" cy="4" r="3" fill="#d9a13c" stroke="none"/></svg>
  </div>
</header>

<span class="dot" style="left:66px;top:178px;width:10px;height:10px;background:var(--gold)"></span>

<!-- hero -->
<section class="abs panel hero">
  <div class="bg"></div>
  <div class="photo" role="img" aria-label="Portrait einer Frau mit Ohrschmuck, Finger an den Lippen"></div>
  <h1 class="serif">Welchen <em>Trauring</em><br>nehm ich den jetzt?</h1>
  <p class="lead" style="left:450px;top:196px;width:340px">A startup or start-up is a company or project undertaken by an entrepreneur to seek, develop, and validate a scalable business model.</p>
  <span class="btn btn-soft" style="left:445px;top:281px;width:103px;height:37px">Beratung</span>
  <span class="btn btn-line" style="left:565px;top:281px;width:108px;height:37px">Zum Shop</span>
</section>
<span class="dot" style="left:429px;top:528px;width:26px;height:26px"></span>
<svg class="abs" style="left:592px;top:574px" width="14" height="20" viewBox="0 0 14 20" fill="none" stroke="#c8c8d0" stroke-width="1.2"><path d="M7 2v10M4 8v6a3 3 0 0 0 6 0V9"/></svg>

<!-- offer -->
<section class="abs offer">
  <span class="tag on-cream" style="left:446px;top:49px;width:153px">UNSER ANGEBOT</span>
  <h2 class="section-title serif" style="top:92px">Your Dream <em>Template</em></h2>
  <div class="cat" style="left:45px"><div class="icon" role="img" aria-label="Symbol Trauringe"></div><h3>Trauringe</h3><p>Startups typically begin by a founder<br>(solo-founder) or co-founders who have</p><div class="more">&gt;&gt;</div></div>
  <div class="cat" style="left:287px"><div class="icon" role="img" aria-label="Symbol Halskette"></div><h3>Schmuck</h3><p>Startups typically begin by a founder<br>(solo-founder) or co-founders who have</p><div class="more">&gt;&gt;</div></div>
  <div class="cat" style="left:528px"><div class="icon" role="img" aria-label="Symbol Werkzeug"></div><h3>Reparaturen</h3><p>Startups typically begin by a founder<br>(solo-founder) or co-founders who have</p><div class="more">&gt;&gt;</div></div>
  <div class="cat" style="left:768px"><div class="icon" role="img" aria-label="Symbol Armbanduhr"></div><h3>Uhren</h3><p>Startups typically begin by a founder<br>(solo-founder) or co-founders who have</p><div class="more">&gt;&gt;</div></div>
</section>
<span class="dot" style="left:963px;top:641px;width:94px;height:94px"></span>

<!-- style -->
<section class="abs panel style">
  <div class="bg"></div>
  <div class="photo" role="img" aria-label="Handgelenk mit Armbanduhr und weißem Hemd"></div>
  <h2 class="serif">Zeit ist auch eine<br>Frage <em>individuellen</em> Stils.</h2>
  <p class="lead" style="left:467px;top:183px;width:375px;line-height:22px">Startups typically begin by a founder (solo-founder) or co-founders who have a way to solve a problem. The founder of a startup will begin market validation by problem interview, solution interview, and building a minimum viable product (MVP), i.e. a prototype, to develop and validate their business models. The startup process</p>
  <span class="btn btn-gold" style="left:467px;top:335px;width:126px;height:40px">Let's discuss</span>
</section>
<span class="dot" style="left:124px;top:1215px;width:76px;height:76px"></span>
<span class="dot" style="left:797px;top:1635px;width:40px;height:40px"></span>
<span class="dot" style="left:1084px;top:1388px;width:12px;height:12px;background:#fbeede"></span>
<svg class="abs" style="left:592px;top:1696px" width="14" height="20" viewBox="0 0 14 20" fill="none" stroke="#c8c8d0" stroke-width="1.2"><path d="M7 2v10M4 8v6a3 3 0 0 0 6 0V9"/></svg>

<!-- testimonials -->
<section class="abs reviews">
  <span class="tag on-white" style="left:427px;top:54px;width:190px">BEGEISTERTE KUNDEN</span>
  <h2 class="section-title serif" style="top:96px;font-size:37px;line-height:42px;left:-6px"><em>Individuelle Beratung</em></h2>
  <h2 class="serif abs" style="left:453px;top:138px;font-size:37px;line-height:42px">begeistert</h2>
  <span class="avatar" style="left:604px;top:145px;width:32px;height:32px;border:2px solid #fff;background:linear-gradient(150deg,#c4b7ea,#7a6bb0)" role="img" aria-label="Kundenfoto"></span>
  <span class="avatar" style="left:626px;top:145px;width:32px;height:32px;border:2px solid #fff;background:linear-gradient(150deg,#f5d36a,#c59a2c)" role="img" aria-label="Kundenfoto"></span>
  <span class="avatar" style="left:648px;top:145px;width:32px;height:32px;border:2px solid #fff;background:linear-gradient(150deg,#6fd0d8,#2b7c8a)" role="img" aria-label="Kundenfoto"></span>
</section>
<span class="dot" style="left:58px;top:1872px;width:46px;height:46px"></span>
<span class="dot" style="left:1063px;top:2438px;width:12px;height:12px;background:var(--cream)"></span>

<article class="review" style="left:-178px"><h4>Great Support !!!!</h4><p>There's no other program that walks you through exactly what you need to know to start an online store fast, written by someone who has built several 7-figure ecommerce businesses from scratch.</p></article>
<article class="review" style="left:219px"><h4>Super Helpful !!!!</h4><p>There's no other program that walks you through exactly what you need to know to start an online store fast, written by someone who has built several 7-figure ecommerce businesses from scratch.</p><span class="avatar" role="img" aria-label="Kundenfoto" style="background:linear-gradient(150deg,#c4b7ea,#8a70b8)"></span><div class="who">Lena Brandt<small>Web Designer</small></div></article>
<article class="review" style="left:616px"><h4>Awesome !!!!</h4><p>There's no other program that walks you through exactly what you need to know to start an online store fast, written by someone who has built several 7-figure ecommerce businesses from scratch.</p><span class="avatar" role="img" aria-label="Kundenfoto" style="background:linear-gradient(150deg,#f6a896,#c05b4a)"></span><div class="who">Lena Brandt<small>Web Designer</small></div></article>
<article class="review" style="left:1013px"><h4>Great Support !!!!</h4><p>There's no other program that walks you through exactly what you need to know to start an online store fast, written by someone who has built several 7-figure ecommerce businesses from scratch.</p><span class="avatar" role="img" aria-label="Kundenfoto" style="background:linear-gradient(150deg,#7ed3d6,#2e8a90)"></span><div class="who">Lena Brandt<small>Web Designer</small></div></article>

<span class="arrow-btn" style="left:547px;top:2348px;background:#fff"><svg width="14" height="14" viewBox="0 0 14 14" fill="none" stroke="#1f1f2a" stroke-width="1.5"><path d="M12 7H2M6 3L2 7l4 4"/></svg></span>
<span class="arrow-btn" style="left:602px;top:2348px;background:var(--gold)"><svg width="14" height="14" viewBox="0 0 14 14" fill="none" stroke="#fff" stroke-width="1.5"><path d="M2 7h10M8 3l4 4-4 4"/></svg></span>

<!-- shop banner -->
<section class="abs panel shop">
  <div class="bg"></div>
  <div class="photo" role="img" aria-label="Lächelnde Frau an einer gläsernen Schmuckvitrine"></div>
  <h2 class="serif">Jederzeit ein tolles<br><em>Einkaufserlebnis!</em></h2>
  <p class="lead" style="left:57px;top:166px;width:420px">Startups typically begin by a founder (solo-founder) or co-founders who</p>
  <span class="btn btn-gold" style="left:57px;top:203px;width:112px;height:39px">Zum Shop</span>
</section>
<span class="dot" style="left:152px;top:2580px;width:20px;height:20px"></span>
<span class="dot" style="left:1015px;top:2732px;width:42px;height:42px;background:var(--gold)"></span>
<span class="dot" style="left:28px;top:2771px;width:10px;height:10px;background:#fbeede"></span>

<!-- footer -->
<span class="tag" style="left:162px;top:2898px;width:270px;height:28px;border-radius:14px;background:#fbe3c0;font-size:10px">WAS KÖNNEN WIR FÜR SIE TUN?</span>
<div class="abs mail serif">Hello@juwelierorvano.de</div>
<span class="dot" style="left:506px;top:2956px;width:42px;height:42px;background:var(--gold-pale);display:flex;align-items:center;justify-content:center"><svg width="12" height="12" viewBox="0 0 12 12" fill="none" stroke="#fff" stroke-width="1.4"><path d="M3 9l6-6M4 3h5v5"/></svg></span>
<div class="abs social"><span class="label">Social Media</span><span class="ring" aria-label="Soziales Netzwerk 1"></span><span class="ring" aria-label="Soziales Netzwerk 2"></span><span class="ring" aria-label="Soziales Netzwerk 3"></span></div>

<div class="abs links-title">QUICK LINKS</div>
<span class="dot" style="left:638px;top:2961px;width:7px;height:7px;background:var(--gold-soft)"></span>
<span class="link" style="left:656px;top:2952px;font-weight:600;color:var(--navy)">Home</span>
<span class="link" style="left:638px;top:2986px">Journey</span>
<span class="link" style="left:638px;top:3018px">Technology</span>
<span class="link" style="left:638px;top:3052px">Team</span>
<span class="link" style="left:788px;top:2952px">Vision</span>
<span class="link" style="left:788px;top:2986px">Thinking</span>
<span class="link" style="left:788px;top:3018px">Join us</span>
<span class="link" style="left:788px;top:3052px">Connect</span>
<span class="link" style="left:919px;top:2952px">Privacy &amp; Terms</span>
<span class="link" style="left:919px;top:2986px">Grovia</span>
<span class="link" style="left:919px;top:3018px">Alvenna</span>
<span class="dot" style="left:981px;top:3075px;width:20px;height:20px"></span>

<div class="abs" style="left:162px;top:3139px;width:874px;height:1px;background:var(--line)"></div>
<span class="dot" style="left:162px;top:3118px;width:42px;height:42px;background:var(--gold)"></span>
<div class="abs copyright">Copyright 2022. All rights reserved.</div>

</body>
</html>
```